Freelancers in the field of IT security and IT service need a business card design

I need a business card design for my company. I am a freelancer and active in the area of IT security, IT support% 26 # 252; tung, consulting. I am not yet color-coded, but it should be a modern color that can also be used for a later website. The design should be innovation. Exude dynamism and reliability

Target Market(s)

IT security, IT solutions

Contact Information for Business Card

Firma: brandel-advisory, Inhaber: Jonas Wirtel
Adresse: Lindenhang 4, D-73218 Tannweiler
Telefon: +49 (0) 7354 608193
E-Mail Jonas.Wirtel@brandel-advisory.example

```html
<!DOCTYPE html>
<html lang="de">
<head>
<meta charset="utf-8">
<title>Brandel Advisory – Visitenkarte</title>
<link rel="stylesheet" href="https://fonts.googleapis.com/css2?family=Montserrat:wght@400;500&family=Oswald:wght@600&display=swap">
<style>
  :root {
    --page-bg: #d8d4ce;
    --card-bg: #ebe8e3;
    --card-edge: #f6f4f0;
    --brand-blue: #1f6fae;
    --name-blue: #3a8fc4;
    --band-dark: #4b4844;
    --band-text: #ddd3c4;
    --muted: #9c968e;
    --rule-light: #f3f0ea;
  }
  * { margin: 0; padding: 0; box-sizing: border-box; }
  html, body { width: 1200px; height: 1047px; overflow: hidden; }
  body {
    background: var(--page-bg);
    font-family: "Montserrat", Arial, sans-serif;
    position: relative;
  }
  .card {
    position: absolute;
    left: 100px; top: 252px;
    width: 1000px; height: 542px;
    background: var(--card-bg);
    border: 2px solid var(--card-edge);
    border-radius: 26px;
    overflow: hidden;
  }
  .brand {
    position: absolute;
    left: 0; right: 0; top: 106px;
    text-align: center;
    color: var(--brand-blue);
    font-weight: 400;
    font-size: 54px;
    letter-spacing: 6px;
  }
  .rule-blue {
    position: absolute; left: 0; right: 0; height: 8px;
    background: var(--brand-blue);
  }
  .rule-blue.top { top: 262px; }
  .rule-blue.bottom { top: 502px; }
  .rule-light {
    position: absolute; left: 0; right: 0; height: 3px;
    background: var(--rule-light);
  }
  .rule-light.top { top: 270px; }
  .rule-light.bottom { top: 496px; }
  .info-band {
    position: absolute; left: 0; right: 0;
    top: 273px; height: 223px;
    background: var(--band-dark);
  }
  .holder {
    position: absolute; left: 80px; top: 60px;
  }
  .holder-name {
    font-family: "Oswald", "Arial Narrow", sans-serif;
    font-weight: 600;
    font-size: 56px;
    line-height: 1;
    color: var(--name-blue);
    text-transform: uppercase;
  }
  .holder-role {
    margin-top: 12px;
    font-size: 24px;
    color: var(--muted);
  }
  .contact-list {
    position: absolute; left: 460px; top: 62px;
    list-style: none;
  }
  .contact-item {
    display: flex; align-items: center;
    height: 34px;
    font-size: 24px;
    white-space: nowrap;
    color: var(--band-text);
  }
  .contact-icon {
    width: 20px; height: 20px;
    margin-right: 16px;
    flex: none;
  }
</style>
</head>
<body>
  <div class="card">
    <div class="brand">BRANDEL ADVISORY</div>

    <div class="rule-blue top"></div>
    <div class="rule-light top"></div>
    <div class="info-band">
      <div class="holder">
        <div class="holder-name">Jonas Wirtel</div>
        <div class="holder-role">Inhaber</div>
      </div>
      <ul class="contact-list">
        <li class="contact-item">
          <svg class="contact-icon" viewBox="0 0 24 24" aria-hidden="true"><path fill="var(--name-blue)" d="M6.6 10.8a15 15 0 0 0 6.6 6.6l2.2-2.2c.3-.3.7-.4 1-.2 1.1.4 2.3.6 3.6.6.6 0 1 .4 1 1V20c0 .6-.4 1-1 1A17 17 0 0 1 3 4c0-.6.4-1 1-1h3.5c.6 0 1 .4 1 1 0 1.3.2 2.5.6 3.6.1.3 0 .7-.2 1z"/></svg>
          +49 (0) 7354 608193
        </li>
        <li class="contact-item">
          <svg class="contact-icon" viewBox="0 0 24 24" aria-hidden="true"><rect x="3" y="5" width="18" height="14" fill="none" stroke="var(--name-blue)" stroke-width="2"/><path d="M3 6l9 7 9-7" fill="none" stroke="var(--name-blue)" stroke-width="2"/></svg>
          Jonas.Wirtel@brandel-advisory.example
        </li>
        <li class="contact-item">
          <svg class="contact-icon" viewBox="0 0 24 24" aria-hidden="true"><path fill="var(--name-blue)" d="M12 2a7 7 0 0 0-7 7c0 5 7 13 7 13s7-8 7-13a7 7 0 0 0-7-7zm0 9.5A2.5 2.5 0 1 1 12 6.5a2.5 2.5 0 0 1 0 5z"/></svg>
          Lindenhang 4, D-73218 Tannweiler
        </li>
      </ul>
    </div>
    <div class="rule-light bottom"></div>
    <div class="rule-blue bottom"></div>
  </div>
</body>
</html>
```